Distilled spirits labels for whiskey, rum, vodka, tequila and moonshine

I am ready to have labels created for a complete line of distilled spirits. I make whiskey, rum, tequila, vodka and moonshine. All my products are aged in oak barrels for at least 18 months or anejo. My company name is Brackenford, Ltd. Aka Brackenford Distillery. I call my whiskey "Tideroamer's " I've included a draft label for it. All are hand made so each may taste a little different. I'll probably want to hand write "batch" and "bottle " number on each bottle. All are 80 proof. My whiskey is lmade with barley. Rum is made with cane sugars and molasses. Tequila is made from organic blue agave. It is made in Kansas, so i don't think that I can call it tequila. The labels will also need to be compliant with u.s. regulations. All are 750 ml bottles. Im open for themes and names.

Target Market(s)

Premium liquor drinkers

Font styles to use
Serif

Colors

Designer to choose colors to be used in the design.

Requirements
Must have
• U.s. compliance, good looking

```html
<!DOCTYPE html>
<html lang="en">
<head>
<meta charset="utf-8">
<title>Tideroamer's Single Barrel Whiskey Label</title>
<link rel="stylesheet" href="https://fonts.googleapis.com/css2?family=Cinzel:wght@600;700&family=Oranienbaum&family=Playfair+Display:wght@700&display=swap">
<style>
  :root {
    --backdrop: #000000;
    --ink: #232323;
    --ink-deep: #151515;
    --gold: #c58b2a;
    --gold-light: #f1cb6c;
    --white: #ffffff;
  }
  html, body {
    margin: 0;
    padding: 0;
    width: 686px;
    height: 1200px;
    overflow: hidden;
    background: var(--backdrop);
  }
  .canvas {
    width: 686px;
    height: 1200px;
    display: flex;
    align-items: center;
    justify-content: center;
  }
  .label { width: 630px; height: 792px; display: block; }
  .frame-gold { fill: none; stroke: url(#goldSheen); stroke-width: 26; }
  .frame-white { fill: none; stroke: var(--white); stroke-width: 16; }
  .frame-body { fill: var(--ink); stroke: var(--gold); stroke-width: 2; }
  .frame-dots { fill: none; stroke: var(--white); stroke-width: 3.2; stroke-dasharray: 0.1 7; stroke-linecap: round; }
  .frame-line { fill: none; stroke: var(--gold); stroke-width: 2; }
  .ribbon { fill: var(--ink); stroke: url(#goldSheen); stroke-width: 4; }
  .ribbon-text { font-family: "Cinzel", serif; font-weight: 700; font-size: 19px; letter-spacing: 3px; fill: var(--white); }
  .brand-name { font-family: "Oranienbaum", serif; font-size: 128px; fill: var(--white); }
  .spirit-type { font-family: "Cinzel", serif; font-weight: 700; font-size: 46px; fill: url(#goldSheen); }
  .strength { font-family: "Cinzel", serif; font-weight: 600; font-size: 32px; fill: var(--white); }
  .banner-outer { fill: var(--white); stroke: url(#goldSheen); stroke-width: 5; }
  .banner-inner { fill: var(--ink-deep); stroke: url(#goldSheen); stroke-width: 3; }
  .distillery { font-family: "Oranienbaum", serif; font-size: 58px; fill: var(--white); }
  .volume { font-family: "Playfair Display", serif; font-weight: 700; font-size: 32px; fill: var(--white); }
</style>
</head>
<body>
<main class="canvas">
  <svg class="label" viewBox="270 160 700 880" xmlns="http://www.w3.org/2000/svg" aria-label="Tideroamer's Single Barrel Whiskey label">
    <defs>
      <linearGradient id="goldSheen" x1="0" y1="0" x2="1" y2="1">
        <stop offset="0" stop-color="#a8731f"/>
        <stop offset="0.45" stop-color="#f1cb6c"/>
        <stop offset="0.7" stop-color="#c58b2a"/>
        <stop offset="1" stop-color="#8f5e16"/>
      </linearGradient>
      <path id="labelShape" d="M385,268 C470,188 770,188 855,268 Q865,372 960,382 L960,688 Q868,692 855,762 L855,970 Q620,1085 385,970 L385,762 Q372,692 280,688 L280,382 Q375,372 385,268 Z"/>
      <path id="ribbonArc" d="M505,290 Q620,232 735,290"/>
      <path id="bannerArc" d="M350,858 Q620,895 890,838"/>
    </defs>

    <!-- label body with layered frame -->
    <use href="#labelShape" class="frame-gold"/>
    <use href="#labelShape" class="frame-white"/>
    <use href="#labelShape" class="frame-body"/>
    <g transform="translate(620 620) scale(0.955 0.962) translate(-620 -620)">
      <use href="#labelShape" class="frame-dots" vector-effect="non-scaling-stroke"/>
    </g>
    <g transform="translate(620 620) scale(0.925 0.935) translate(-620 -620)">
      <use href="#labelShape" class="frame-line" vector-effect="non-scaling-stroke"/>
    </g>

    <!-- finest quality ribbon -->
    <path class="ribbon" d="M478,298 L500,268 Q620,220 742,268 L762,300 L742,302 L735,320 Q620,272 505,320 L498,302 Z"/>
    <path class="ribbon" d="M500,268 Q620,220 742,268 L735,320 Q620,272 505,320 Z"/>
    <text class="ribbon-text" text-anchor="middle">
      <textPath href="#ribbonArc" startOffset="50%">FINEST QUALITY</textPath>
    </text>

    <!-- emblem area -->
    <rect role="img" aria-label="Gold heraldic creature emblem" x="530" y="322" width="160" height="120" rx="18" fill="url(#goldSheen)"/>

    <!-- product naming -->
    <text class="brand-name" x="620" y="572" text-anchor="middle" textLength="560" lengthAdjust="spacingAndGlyphs">TIDEROAMER’S</text>
    <text class="spirit-type" x="620" y="648" text-anchor="middle">S<tspan font-size="36">INGLE</tspan> B<tspan font-size="36">ARREL</tspan></text>
    <text class="spirit-type" x="620" y="716" text-anchor="middle">W<tspan font-size="36">HISKEY</tspan></text>
    <text class="strength" x="620" y="776" text-anchor="middle">40 % A<tspan font-size="25">LC</tspan></text>

    <!-- distillery banner -->
    <path class="banner-outer" d="M345,762 Q620,812 897,760 L927,888 Q620,944 314,886 Z"/>
    <path class="banner-inner" d="M360,788 Q620,832 882,784 L906,866 Q620,918 334,868 Z"/>
    <text class="distillery" text-anchor="middle" textLength="530" lengthAdjust="spacingAndGlyphs">
      <textPath href="#bannerArc" startOffset="50%">BRACKENFORD’S DISTILLERY</textPath>
    </text>

    <!-- volume -->
    <text class="volume" x="620" y="962" text-anchor="middle">vol 750 ml</text>
  </svg>
</main>
</body>
</html>
```